Mexican Restaurant - Flyer for takeaway and delivery customers

We are a Mexican Restaurant.  We need a flyer for home delivery customers...should include our menu, photos, prices and location etc....
I have attached our menu, logo and some photos...feel free to use some of your own.  Please ask if you have any questions.
we prefer a one page (front and back) A4 or A5 size.  If that is not possible because of the number of items, maybe a booklet type flyer is acceptable.
WE also need the following text:
Salsa Verdal - New in KMBQ!
Unit R7-23
Level R7
Gable Heights
Kestrel Meridian Business Quarter
The phone number of :  04 318 5902
And the verbiage "Free Parking Available"!
Please reference the colors on the examples provided
If you can use Minion Pro font that would be great

```html
<!DOCTYPE html>
<html lang="en">
<head>
<meta charset="utf-8">
<title>Salsa Verdal – Takeaway Menu Flyer</title>
<link rel="stylesheet" href="https://fonts.googleapis.com/css2?family=Alfa+Slab+One&family=Crimson+Pro:ital,wght@0,400;0,600;1,400;1,600&family=Graduate&family=Pathway+Gothic+One&display=swap">
<style>
  :root{
    --red:#e6283a;
    --blue:#29b5e6;
    --brown:#3a2322;
    --ink:#231a1a;
    --white:#ffffff;
    --paper:#e9e9ec;
    --slab:"Alfa Slab One", serif;
    --serif:"Crimson Pro", serif;
    --college:"Graduate", serif;
    --cond:"Pathway Gothic One", sans-serif;
  }
  *{box-sizing:border-box;margin:0;padding:0}
  html,body{width:959px;height:1200px;overflow:hidden}
  body{background:var(--paper);position:relative;font-family:var(--serif);color:var(--ink)}

  .spread{position:absolute;left:69px;width:820px;height:580px;overflow:hidden;box-shadow:0 2px 6px rgba(0,0,0,.18)}
  .spread--inside{top:14px;background:var(--white)}
  .spread--cover{top:606px;background:var(--brown)}

  .pattern-frame{position:absolute;inset:0}
  .spread--inside .pattern-frame{background:linear-gradient(90deg,#f2b3b9,#b4e2f3,#f2b3b9,#b4e2f3)}
  .spread--cover .pattern-frame{background:linear-gradient(90deg,#4a2a2f,#2f3b4c,#4a2a2f,#2f3b4c)}
  .sheet{position:absolute;background:var(--white)}
  .sheet--left{left:22px;top:22px;width:378px;height:536px}
  .sheet--right{left:420px;top:22px;width:378px;height:536px}
  .fold-line{position:absolute;left:410px;top:0;height:580px;border-left:1px dashed #8a8a8a}

  .section-title{font-family:var(--slab);font-size:16px;letter-spacing:.5px;line-height:1}
  .blue{color:var(--blue)} .red{color:var(--red)}
  .item{margin-top:3px}
  .item-name{font-family:var(--serif);font-weight:600;font-size:11px;line-height:1.1}
  .price-line{display:flex;align-items:baseline;font-family:var(--cond);font-size:7.6px;line-height:1.25;color:var(--ink)}
  .price-line .leader{flex:1;border-bottom:1px dotted currentColor;margin:0 2px;min-width:6px}
  .price-line b{font-weight:400;color:var(--red);white-space:nowrap}
  .block{position:absolute}

  .photo{position:absolute}

  .tilt-square{position:absolute;background:var(--blue)}
  .dark-card{position:absolute;background:var(--brown);border-radius:8px;color:var(--white);padding:10px}
  .dark-card .price-line{color:var(--white)}
  .dark-card .price-line b{color:var(--white)}
  .card-title{font-family:var(--serif);font-weight:600;font-size:17px;color:var(--red);text-align:right}
  .card-sub{font-family:var(--cond);font-size:7.6px;color:var(--blue);line-height:1.3;margin:6px 0}

  .hawaiana{display:flex;align-items:center;gap:6px;background:var(--brown);border-radius:6px;padding:4px 8px;margin:5px 0 3px;height:38px;color:var(--white)}
  .hawaiana .item-name{color:var(--blue);font-size:12px}
  .hawaiana p{font-family:var(--cond);font-size:7.4px;line-height:1.25;flex:1}
  .hawaiana b{font-family:var(--cond);font-weight:400;font-size:8px}

  .grill-title{font-family:var(--slab);color:var(--red);font-size:15px;line-height:1.05;text-align:right}
  .grill-rule{position:absolute;left:488px;top:44px;width:2px;height:84px;background:var(--ink)}

  .tinga{position:absolute;left:426px;top:156px;width:355px;height:84px;background:var(--red);border-radius:8px;padding:6px 10px;color:var(--white)}
  .tinga .price-line,.tinga .price-line b{color:var(--white)}
  .tinga .item-name{font-size:11px}

  .burrito-title{font-family:var(--slab);font-size:13.5px;line-height:1.1;text-align:center}
  .burrito-text{font-family:var(--cond);font-size:7.6px;line-height:1.35;margin-top:8px}

  .panel{position:absolute;top:34px;width:342px;height:507px;overflow:hidden}
  .panel--back{left:34px}
  .panel--front{left:443px}
  .panel svg.panel-art{position:absolute;inset:0}
  .headline-new{position:absolute;left:34px;top:42px;font-family:var(--slab);font-weight:400;font-size:36px;line-height:1.12;color:var(--brown)}
  .address{position:absolute;left:34px;top:268px;font-family:var(--serif);font-style:normal;font-size:14px;line-height:1.3;color:var(--white)}
  .cover-phone{position:absolute;left:34px;top:380px;font-family:var(--serif);font-size:15px;color:var(--red);display:flex;align-items:center;gap:6px}
  .parking{position:absolute;left:34px;top:404px;font-family:var(--serif);font-weight:600;font-size:13px;color:var(--white)}
  .wordmark{position:absolute;font-family:var(--serif);font-weight:400;line-height:1;white-space:nowrap}
  .tagline{position:absolute;font-family:var(--serif);font-size:7px;letter-spacing:.6px;white-space:nowrap}
  .tasty{position:absolute;right:34px;top:245px;font-family:var(--college);font-size:46px;color:var(--white);line-height:1}
  .mexican{position:absolute;left:34px;top:312px;font-family:var(--college);font-size:26px;color:var(--white);line-height:1}
  .call{position:absolute;left:0;width:290px;text-align:right;top:430px;font-family:var(--college);font-size:25px;color:var(--white);line-height:1}
  .call-number{position:absolute;left:0;width:330px;text-align:right;top:465px;font-family:var(--slab);font-size:20px;color:var(--red);line-height:1}
</style>
</head>
<body>

<section class="spread spread--inside" aria-label="Inside menu spread">
  <div class="pattern-frame" role="img" aria-label="Border of red and blue Mexican diamond and triangle pattern"></div>
  <div class="sheet sheet--left"></div>
  <div class="sheet sheet--right"></div>
  <div class="fold-line"></div>

  <div class="block" style="left:42px;top:44px;width:208px">
    <h2 class="section-title blue">APPETIZERS</h2>
    <div class="item"><h3 class="item-name red">Guacamole</h3>
      <p class="price-line"><span>Served with our home-made corn tortilla chips (250g)</span><i class="leader"></i><b>AED 42.00</b></p>
      <p class="price-line"><span>With our Gourmet in-house tortilla chips (250 g)</span><i class="leader"></i><b>AED 48.00</b></p></div>
    <div class="item"><h3 class="item-name blue">Salsa Verdal Nachos</h3>
      <p class="price-line"><span>Traditional (no meat)</span><i class="leader"></i><b>AED 32.00</b></p>
      <p class="price-line"><span>With either pastor (marinated steak), steak or chicken</span><i class="leader"></i><b>AED 44.00</b></p></div>
    <div class="item"><h3 class="item-name red">Empanaditas</h3>
      <p class="price-line"><span>Stuffed with chicken</span><i class="leader"></i><b>AED 17.00</b></p>
      <p class="price-line"><span>Cheese</span><i class="leader"></i><b>AED 22.00</b></p></div>
    <div class="item"><h3 class="item-name blue">Tacos dorados</h3>
      <p class="price-line"><span>Served with fresh lettuce, tomato, cream and cheese</span><i class="leader"></i><b>AED 19.00</b></p></div>
  </div>

  <div class="tilt-square" style="left:262px;top:64px;width:140px;height:110px;transform:rotate(8deg)"></div>
  <div class="dark-card" style="left:258px;top:94px;width:136px;height:170px">
    <h3 class="card-title">Quesadilla</h3>
    <p class="card-sub">with melted cheese<br>served with cream and a dab of guacamole</p>
    <p class="price-line"><span>Quesadilla with melted cheese, cream and guacamole</span><i class="leader"></i><b>AED 20.00</b></p>
    <p class="price-line"><span>Mushrooms</span><i class="leader"></i><b>AED 25.00</b></p>
    <p class="price-line"><span>Pastor (marinated steak), steak or chicken</span><i class="leader"></i><b>AED 30.00</b></p>
  </div>

  <div class="block" style="left:42px;top:262px;width:348px">
    <h2 class="section-title red">TACOS</h2>
    <div class="item"><h3 class="item-name blue">Ketaco</h3>
      <p class="price-line"><span>A hard taco shell made with cheese! Filled with your favourite pastor (marinated steak), steak or chicken</span><i class="leader"></i><b>AED 37.00</b></p></div>
    <div class="item"><h3 class="item-name red">Gringa</h3>
      <p class="price-line"><span>Two flour tortillas with pastor (marinated steak) grilled in cheese, coriander, onion and pineapple!</span><i class="leader"></i><b>AED 37.00</b></p></div>
    <div class="item"><h3 class="item-name blue">Tacos al pastor</h3>
      <p class="price-line"><span>Marinated steak - Corn tortilla (order of 3) Flour tortilla (order of 2)</span><i class="leader"></i><b>AED 30.00</b></p>
      <p class="price-line"><span>Add cheese</span><i class="leader"></i><b>AED +5.00</b></p></div>
    <div class="item"><h3 class="item-name red">Mula terca</h3>
      <p class="price-line"><span>Two flour tortillas with steak, beef bacon and melted cheese</span><i class="leader"></i><b>AED 40.00</b></p></div>
    <div class="hawaiana">
      <h3 class="item-name">Hawaiana</h3>
      <p>Salsa Verdal's secret: chicken, turkey breast ham, pineapple, beef bacon and cheese all inside three flour tortillas</p>
      <div role="img" aria-label="Photo of a grilled Hawaiana taco" style="width:46px;height:30px;border-radius:50%;background:radial-gradient(circle,#f2d9a8,#c77a3d)"></div>
      <b>AED 48.00</b>
    </div>
    <div class="item"><h3 class="item-name red">Chicken or steak</h3>
      <p class="price-line"><span>Corn tortilla (order of 3) Flour tortilla (order of 2) Cheese tortilla (order of 1)</span><i class="leader"></i><b>AED 30.00</b></p>
      <p class="price-line"><span>Add cheese</span><i class="leader"></i><b>AED +5.00</b></p></div>
    <div class="item"><h3 class="item-name blue">Veggie</h3>
      <p class="price-line"><span>Corn tortilla (order of 3) Flour tortilla (order of 2) Cheese tortilla (order of 1)</span><i class="leader"></i><b>AED 30.00</b></p>
      <p class="price-line"><span>Add cheese</span><i class="leader"></i><b>AED +5.00</b></p></div>
  </div>

  <h2 class="grill-title block" style="left:426px;top:46px;width:56px">FROM<br>THE<br>GRILL</h2>
  <div class="grill-rule"></div>
  <div class="block" style="left:496px;top:42px;width:290px">
    <div class="item" style="margin-top:0"><h3 class="item-name blue">Sope</h3>
      <p class="price-line"><span>Served with refried beans, lettuce, cream and velvety cheese</span><i class="leader"></i><b>AED 27.00</b></p></div>
    <div class="item"><h3 class="item-name red">Huarache</h3>
      <p class="price-line"><span>Slightly thicker corn tortilla served with refried beans, cheese, lettuce, avocado, green or red salsa and the meat of your choice: pastor, steak or chicken</span><i class="leader"></i><b>AED 39.00</b></p></div>
    <div class="item"><h3 class="item-name blue">Volcan</h3>
      <p class="price-line"><span>3 crispy corn tortillas served with melted cheese and steak</span><i class="leader"></i><b>AED 48.00</b></p></div>
  </div>

  <div class="tinga">
    <div style="width:240px">
      <h3 class="item-name">Tinga quesadilla</h3>
      <p class="price-line"><span>Corn tortilla served with freshly seasoned pulled chicken marinated in a fresh tomato base, served with refried beans, cheese, onion, coriander and fresh tomato</span><i class="leader"></i><b>AED 40.00</b></p>
      <p class="price-line"><span>With mushrooms</span><i class="leader"></i><b>AED 44.00</b><span style="margin-left:10px">Add extra cheese</span><i class="leader"></i><b>AED 47.00</b></p>
    </div>
  </div>
  <div class="photo" role="img" aria-label="Photo of tinga quesadilla with fresh salad" style="left:684px;top:150px;width:94px;height:90px;border-radius:6px;transform:rotate(6deg);background:linear-gradient(160deg,#e2b36e,#c8853f 45%,#e9e4dc 60%,#6f9a45)"></div>

  <div class="block" style="left:426px;top:256px;width:214px">
    <h2 class="section-title blue">ALAMBRES</h2>
    <div class="item"><h3 class="item-name red">Alambre traditional</h3>
      <p class="price-line"><span>Beef bacon, bell peppers, onion, melted cheese with your choice of meat: pastor, steak or chicken</span><i class="leader"></i><b>AED 50.00</b></p></div>
    <div class="item"><h3 class="item-name blue">Alambre de barrio</h3>
      <p class="price-line"><span>All of your favorites from the Alambre traditional but with a mix of pastor (marinated steak) and steak</span><i class="leader"></i><b>AED 55.00</b></p></div>
    <div class="item"><h3 class="item-name red">Vegetarian alambre</h3>
      <p class="price-line"><span>Onion, bell peppers, mushrooms and cheese</span><i class="leader"></i><b>AED 47.00</b></p></div>

    <h2 class="section-title red" style="margin-top:14px">DESSERTS</h2>
    <div class="item"><h3 class="item-name blue">Arroz con leche</h3>
      <p class="price-line"><span>Mexico's rice pudding, with a touch of cinnamon to make it more delicious</span><i class="leader"></i><b>AED 18.00</b></p></div>
    <div class="item"><h3 class="item-name red">Flan</h3>
      <p class="price-line"><span>Custard base dessert with a flavorful caramel on top</span><i class="leader"></i><b>AED 10.00</b></p></div>
    <div class="item"><h3 class="item-name blue">Fruit chamoy</h3>
      <p class="price-line"><span>A salty, sour and mild spice sauce drizzled over fresh fruit</span><i class="leader"></i><b>AED 15.00</b></p></div>
  </div>

  <div class="tilt-square" style="left:650px;top:420px;width:112px;height:96px;transform:rotate(22deg)"></div>
  <div class="dark-card" style="left:652px;top:266px;width:128px;height:212px;padding:8px 9px">
    <h3 class="burrito-title"><span class="blue">MAKE<br>YOUR OWN</span><br><span class="red">BURRITO!</span></h3>
    <p class="burrito-text">Base includes: lettuce, refried beans or black beans, cream and cheese.</p>
    <div class="burrito-text">
      <p class="price-line"><span>Normal size</span><i class="leader"></i><b>AED 16.00</b></p>
      <p class="price-line"><span>Mega size</span><i class="leader"></i><b>AED 21.00</b></p>
      <p>Your choice of meat (150g):</p>
      <p class="price-line"><span>Pastor / Steak / chicken</span><i class="leader"></i><b>AED +10.00</b></p>
    </div>
  </div>
</section>

<section class="spread spread--cover" aria-label="Cover spread">
  <div class="pattern-frame" role="img" aria-label="Border of red and blue Mexican triangle pattern on dark brown"></div>

  <div class="panel panel--back">
    <svg class="panel-art" width="342" height="507" viewBox="0 0 342 507" aria-hidden="true">
      <defs>
        <linearGradient id="cityTone" x1="0" y1="0" x2="0" y2="1">
          <stop offset="0" stop-color="#4a3a36"/><stop offset="1" stop-color="#2a1d1c"/>
        </linearGradient>
        <linearGradient id="foodToneBack" x1="0" y1="0" x2="1" y2="1">
          <stop offset="0" stop-color="#2aa9d8"/><stop offset=".6" stop-color="#1d5f86"/><stop offset="1" stop-color="#1b2738"/>
        </linearGradient>
      </defs>
      <rect width="342" height="507" fill="url(#cityTone)" role="img" aria-label="Photo of city towers at dusk"/>
      <polygon points="160,507 342,87 342,507" fill="url(#foodToneBack)" role="img" aria-label="Close-up photo of a taco plate"/>
      <polygon points="0,0 342,0 342,87 0,255" fill="var(--red)"/>
    </svg>
    <h1 class="headline-new">NEW<br>IN KMBQ!</h1>
    <address class="address">Unit R7-23<br>Level R7<br>Gable Heights<br>Kestrel Meridian<br>Business Quarter</address>
    <p class="cover-phone">
      <svg width="12" height="16" viewBox="0 0 12 16" aria-hidden="true"><path d="M3 1 L5 1 L6 4 L4 5.5 Q5 9 7 11 L8.5 9.8 L11 11 L11 13.5 Q9 15.5 6 13 Q1 8 1.5 3 Z" fill="var(--red)"/></svg>
      04 318 5902
    </p>
    <p class="parking">Free Parking Available!</p>
    <p class="wordmark" style="left:186px;top:432px;font-size:24px;color:var(--white)">Salsa Verdal</p>
    <p class="tagline" style="left:206px;top:460px;color:var(--white)">AUTHENTIC MEXICAN FOOD</p>
  </div>

  <div class="panel panel--front">
    <svg class="panel-art" width="342" height="507" viewBox="0 0 342 507" aria-hidden="true">
      <defs>
        <linearGradient id="foodToneFront" x1="0" y1="0" x2="1" y2="1">
          <stop offset="0" stop-color="#35c0ea"/><stop offset=".5" stop-color="#1f7fae"/><stop offset="1" stop-color="#1c3550"/>
        </linearGradient>
      </defs>
      <rect width="342" height="507" fill="var(--brown)"/>
      <polygon points="0,150 342,300 342,507 0,507" fill="url(#foodToneFront)" role="img" aria-label="Close-up photo of tacos with fresh toppings"/>
      <polygon points="0,120 150,148 240,180 300,40 342,10 342,275 250,345 190,420 120,370 0,330" fill="var(--red)"/>
      <polygon points="190,507 342,290 342,507" fill="#1b2334"/>
    </svg>
    <p class="wordmark" style="left:64px;top:44px;font-size:36px;color:var(--red)">Salsa Verdal</p>
    <p class="tagline" style="left:98px;top:88px;color:var(--blue);font-size:8px">AUTHENTIC MEXICAN FOOD</p>
    <p class="tasty">TASTY</p>
    <p class="mexican">MEXICAN FOOD</p>
    <p class="call">CALL</p>
    <p class="call-number">04 318 5902</p>
  </div>
</section>

</body>
</html>
```